program promotional Information booklets used for marketing and information

We need someone to take our two word documents and work some graphic design magic to make it look more professional and inviting. These documents are used for potential new customers. Our target audience is youth and young adults with disabilities and their families. Our website will help to provide our current style www.brightpathways.com.au and our logo will set the colour palette. We want the booklets to convey a culture of fun, innovation, energy & creativity. We do not want to look like a corporate or formal organisation. We want to look more organic and grassroots. The booklets will be distributed as electronic documents and printed in-house. Ideally we would like to still be able to edit the final document in case our prices or services change in the future.

Target Market(s)

Youth and Young adults with special needs

Industry/Entity Type

Community Service

Font styles to use
Sans Serif

Requirements
Must have
• The photos provided relate to the Wayfinder booklet. This program is for those with more profound disabilities. The Uplift program is for those with less support needs, generally not in wheelchairs, but who may have some mobility challenges and mild intellectual disabilities. As you will see our business name is Bright Pathways and this is what we attempt to do for all the young people we work with. We do not focus on their disability but rather on their unique abilities and what they can achieve. In both programs we look to achieve social inclusion in the general community as much as possible.
Nice to have
• Wants to feel high energy, fun, innovative and creative. Could use some stock images in the Uplift booklet if you wanted to. Some of the activities this program will do include: organic gardening, cooking, music, dance and drama, art, life skills, mastering public transport, exercise, etc.
Should not have
• should not focus on disability stereotypes. Should not be too childish.

```html
<!DOCTYPE html>
<html lang="en">
<head>
<meta charset="utf-8">
<title>Uplift 2016 Information Booklet – Bright Pathways</title>
<link rel="stylesheet" href="https://fonts.googleapis.com/css2?family=Orbitron:wght@800&family=Varela+Round&family=Open+Sans:wght@400&display=swap">
<style>
  :root {
    --paper: #e6e7e8;
    --coral: #ef5056;
    --teal: #45b3ad;
    --purple: #9260a8;
    --charcoal: #3d3d3f;
    --white: #ffffff;
    --photo-wall: #7d8494;
    --photo-shirt: #4b556d;
    --photo-carpet: #252a38;
    --photo-bricks: #8a6a55;
  }
  html, body {
    margin: 0;
    padding: 0;
    overflow: hidden;
    background: var(--paper);
  }
  .cover {
    position: relative;
    width: 848px;
    height: 1200px;
    overflow: hidden;
    background: var(--paper);
  }
  .cover-shapes {
    position: absolute;
    inset: 0;
    display: block;
  }
  .brand {
    position: absolute;
    left: 28px;
    top: 520px;
    display: flex;
    align-items: center;
    gap: 12px;
    font-family: "Varela Round", sans-serif;
    font-size: 34px;
    color: var(--purple);
  }
  .brand-dot {
    width: 18px;
    height: 18px;
    border-radius: 50%;
    background: var(--purple);
  }
  .title {
    margin: 0;
    font-family: "Orbitron", sans-serif;
    font-weight: 800;
    color: var(--white);
  }
  .title-line {
    position: absolute;
    left: 428px;
    width: 394px;
    display: block;
    line-height: 1;
    white-space: nowrap;
  }
  .title-program { top: 735px; font-size: 92px; }
  .title-year { top: 815px; font-size: 138px; letter-spacing: -2px; }
  .title-sub { top: 945px; font-size: 27px; letter-spacing: 0; }
  .contact {
    position: absolute;
    left: 0;
    right: 0;
    top: 1087px;
    margin: 0;
    font-family: "Open Sans", sans-serif;
    font-size: 16px;
    line-height: 21.5px;
    color: var(--white);
    text-align: center;
    font-style: normal;
  }
</style>
</head>
<body>
<main class="cover">
  <svg class="cover-shapes" width="848" height="1200" viewBox="0 0 848 1200">
    <defs>
      <clipPath id="photo-frame">
        <polygon points="140,0 848,0 848,330 418,565"/>
      </clipPath>
      <linearGradient id="photo-tone" x1="0.1" y1="0" x2="0.6" y2="1">
        <stop offset="0" stop-color="var(--photo-wall)"/>
        <stop offset="0.3" stop-color="var(--photo-shirt)"/>
        <stop offset="0.65" stop-color="var(--photo-carpet)"/>
        <stop offset="1" stop-color="var(--photo-bricks)"/>
      </linearGradient>
    </defs>

    <polygon class="photo-edge" points="128,0 140,0 418,565 406,560" fill="var(--teal)"/>
    <g clip-path="url(#photo-frame)">
      <rect class="photo" x="0" y="0" width="848" height="600" fill="url(#photo-tone)"
            role="img" aria-label="Photo of young people sitting on a carpet building with coloured toy bricks"/>
    </g>

    <polygon class="band-coral" points="848,330 848,1200 0,1200 0,1045" fill="var(--coral)"/>
    <polygon class="band-teal" points="0,830 848,325 848,335 62,1045 0,1045" fill="var(--teal)"/>
    <polygon class="stripe-purple" points="62,1045 848,335 848,347 76,1045" fill="var(--purple)"/>
    <polygon class="stripe-charcoal" points="76,1045 848,347 848,362 128,1026 122,1045" fill="var(--charcoal)"/>
  </svg>

  <div class="brand">
    <span class="brand-dot"></span>
    <span class="brand-name">Bright Pathways</span>
  </div>

  <h1 class="title">
    <span class="title-line title-program">UPLIFT</span>
    <span class="title-line title-year">2016</span>
    <span class="title-line title-sub">INFORMATION BOOKLET</span>
  </h1>

  <address class="contact">
    Hub Locations: 14 Carrow St, Redbank 6/88 Wattlegrove Rd, Kenmore<br>
    Email: info@brightpathways.com.au<br>
    Postal Address: PO Box 27, Milton DC, 4064<br>
    Phone: 1300 482 917
  </address>
</main>
</body>
</html>
```